Banner signature

Hi, looking for a banner for email signature 728 px wide and 200 px high
Could we have our 10 year logo and premium logo, a similar look and feel of our previous banner design (I've attached) and also include an aboriginal design with the Wording
This email comes to you from Gubbi Gubbi country
I've attached an example of some look and feels that we like.
Can we have the background of banner the Blue colour of our Fern & Tide logo and

```html
<!DOCTYPE html>
<html lang="en">
<head>
<meta charset="utf-8">
<title>Gubbi Gubbi Country – Email Signature Banner</title>
<link rel="stylesheet" href="https://fonts.googleapis.com/css2?family=Comic+Neue:wght@400;700&family=Montserrat:wght@700&display=swap">
<style>
  :root {
    --navy: #001844;
    --sky: #00aeef;
    --white: #ffffff;
    --black: #000000;
    --gold-light: #f6e08a;
    --gold: #d4a62a;
    --gold-dark: #9c7414;
  }
  html, body {
    margin: 0;
    width: 1200px;
    height: 931px;
    overflow: hidden;
    background: var(--white);
  }
  .sheet {
    position: relative;
    width: 1200px;
    height: 931px;
  }
  .banner {
    position: absolute;
    left: 92px;
    width: 1033px;
    height: 284px;
    display: block;
    filter: drop-shadow(9px 9px 6px rgba(0, 0, 0, 0.55));
  }
  .banner--light {
    top: 118px;
    --banner-bg: var(--white);
    --banner-gap: var(--white);
    --banner-text: var(--navy);
    --banner-rule: var(--navy);
  }
  .banner--dark {
    top: 500px;
    --banner-bg: var(--black);
    --banner-gap: var(--black);
    --banner-text: var(--sky);
    --banner-rule: var(--white);
  }
  .banner__bg { fill: var(--banner-bg); }
  .shape-navy { fill: var(--navy); }
  .shape-sky { fill: var(--sky); }
  .line-sky { fill: none; stroke: var(--sky); stroke-linejoin: miter; }
  .line-gap { fill: none; stroke: var(--banner-gap); stroke-linejoin: miter; }
  .badge-seal { fill: url(#gold-sheen); }
  .intro-line {
    font-family: "Comic Neue", "Comic Sans MS", cursive;
    font-weight: 400;
    font-size: 62px;
    fill: var(--banner-text);
  }
  .country-name {
    font-family: "Montserrat", "Century Gothic", sans-serif;
    font-weight: 700;
    font-size: 100px;
    fill: var(--sky);
  }
  .country-rule { stroke: var(--banner-rule); stroke-width: 5; }
  .country-word {
    font-family: "Comic Neue", "Comic Sans MS", cursive;
    font-weight: 400;
    font-size: 60px;
    fill: var(--banner-text);
  }
  .brand-name {
    font-family: "Comic Neue", "Comic Sans MS", cursive;
    font-weight: 700;
    font-size: 31px;
    fill: var(--navy);
  }
</style>
</head>
<body>
<div class="sheet">

  <svg width="0" height="0" style="position:absolute" aria-hidden="true">
    <defs>
      <radialGradient id="gold-sheen" cx="40%" cy="35%" r="70%">
        <stop offset="0" stop-color="var(--gold-light)" style="stop-color:#f6e08a"/>
        <stop offset="0.6" stop-color="#d4a62a"/>
        <stop offset="1" stop-color="#9c7414"/>
      </radialGradient>
      <symbol id="banner-art" viewBox="0 0 1881 517">
        <rect class="banner__bg" x="0" y="0" width="1881" height="517"/>

        <!-- left corner wedge -->
        <polygon class="shape-sky" points="0,0 190,0 0,103"/>

        <!-- left navy diagonal band -->
        <polygon class="shape-navy" points="353,0 738,0 478,150 540,268 540,380 303,517 80,517 80,420 158,373 158,272 130,256 130,145"/>
        <!-- left sky outline stripe -->
        <polyline class="line-sky" stroke-width="15" points="330,0 111,117 111,252 149,272 149,358 61,408 61,517"/>

        <!-- left hexagon frame -->
        <polygon class="shape-navy line-sky" stroke-width="15" points="333,78 488,168 488,350 333,440 176,350 176,168"/>
        <!-- anniversary seal -->
        <circle class="badge-seal" cx="333" cy="252" r="115" role="img" aria-label="Ten year anniversary seal"/>

        <!-- right sky band -->
        <polygon class="shape-sky" points="1478,140 1788,0 1881,0 1881,282 1638,407 1478,315"/>
        <polyline class="line-gap" stroke-width="9" points="1775,0 1497,150 1497,305 1638,386 1881,258"/>
        <polygon class="shape-sky" points="1515,152 1795,0 1881,0 1881,248 1638,380 1515,300"/>

        <!-- right hexagon frame -->
        <polygon class="shape-sky" points="1641,110 1760,178 1760,305 1641,372 1522,305 1522,178"/>
        <polygon class="line-gap" stroke-width="6" points="1641,122 1750,184 1750,298 1641,360 1532,298 1532,184"/>
        <polygon class="shape-navy" points="1641,135 1738,190 1738,292 1641,347 1544,292 1544,190"/>

        <!-- right lower corner -->
        <polygon class="shape-navy" points="1453,517 1743,385 1818,430 1818,517"/>
        <polygon class="shape-sky" points="1762,377 1881,312 1881,517 1838,517 1838,418"/>
        <polyline class="line-gap" stroke-width="8" points="1785,374 1856,412 1856,517"/>
      </symbol>
    </defs>
  </svg>

  <svg class="banner banner--light" viewBox="0 0 1881 517" role="img" aria-label="This email comes to you from Gubbi Gubbi country">
    <use href="#banner-art"/>
    <circle class="badge-seal" cx="1641" cy="240" r="95"/>
    <text class="brand-name" x="1641" y="251" text-anchor="middle">Fern &amp; Tide</text>
    <text class="intro-line" x="546" y="222" textLength="909" lengthAdjust="spacingAndGlyphs">THIS EMAIL COMES TO YOU FROM</text>
    <text class="country-name" x="645" y="342" textLength="703" lengthAdjust="spacingAndGlyphs">GUBBI GUBBI</text>
    <line class="country-rule" x1="655" y1="360" x2="1344" y2="360"/>
    <text class="country-word" x="968" y="430" text-anchor="middle">COUNTRY</text>
  </svg>

  <svg class="banner banner--dark" viewBox="0 0 1881 517" role="img" aria-label="This email comes to you from Gubbi Gubbi country">
    <use href="#banner-art"/>
    <circle class="badge-seal" cx="1641" cy="240" r="95"/>
    <text class="brand-name" x="1641" y="251" text-anchor="middle">Fern &amp; Tide</text>
    <text class="intro-line" x="546" y="222" textLength="909" lengthAdjust="spacingAndGlyphs">THIS EMAIL COMES TO YOU FROM</text>
    <text class="country-name" x="645" y="342" textLength="703" lengthAdjust="spacingAndGlyphs">GUBBI GUBBI</text>
    <line class="country-rule" x1="655" y1="360" x2="1344" y2="360"/>
    <text class="country-word" x="968" y="430" text-anchor="middle">COUNTRY</text>
  </svg>

</div>
</body>
</html>
```